Bewerbungs-Template
Zielgruppe
Ich bin einen Einzelperson und möchte meine Bewerbungsunterlagen überarbeiten. Meine Zielgruppe ist ein potentieller Arbeitgeber welcher überzeugen möchte.
Aufgabenstellung
Das Design sollte professionell und übersichtlich aussehen und ein bisschen einzigartig sein. Es sollte nicht nur ein Deckblatt sein, wichtig ist für mich vor allem die CV-Gestaltung. Es muss kein Word-Format sein, kann mit den gängigen Office oder Photoprogrammen erstellt werden. In meinem Kopf schwirrt eine schlichte Idee mit einem Bordeaux-Roten Highlight herum, vlt. hat jemand eine Gute Idee :)
Ich bedanke mich bereits im Voraus für alle Ideen.

```html
<!DOCTYPE html>
<html lang="de">
<head>
<meta charset="utf-8">
<title>Anschreiben – Heike Brandt</title>
<link rel="stylesheet" href="https://fonts.googleapis.com/css2?family=Noto+Sans:wght@300;400;700&display=swap">
<style>
  :root {
    --bordeaux: #86263a;
    --ink: #1a1a1a;
    --paper: #ffffff;
    --signature-tone: #d9d4d5;
  }
  * { margin: 0; padding: 0; box-sizing: border-box; }
  html, body { width: 849px; height: 1200px; overflow: hidden; background: var(--paper); }
  .letter {
    position: relative;
    width: 849px;
    height: 1200px;
    font-family: "Noto Sans", sans-serif;
    font-weight: 300;
    color: var(--ink);
  }
  .band { position: absolute; left: 0; width: 100%; height: 15px; background: var(--bordeaux); }
  .band--top { top: 0; }
  .band--bottom { bottom: 0; }
  .date {
    position: absolute;
    right: 112px;
    top: 22px;
    font-size: 26px;
    letter-spacing: 3px;
    color: var(--bordeaux);
  }
  .subject {
    position: absolute;
    left: 116px;
    top: 201px;
    font-size: 29px;
    letter-spacing: 1px;
    white-space: nowrap;
  }
  .subject__role { color: var(--bordeaux); }
  .salutation {
    position: absolute;
    left: 161px;
    top: 318px;
    font-size: 21px;
    letter-spacing: 0.8px;
  }
  .accent-rule {
    position: absolute;
    left: 115px;
    top: 393px;
    width: 1.5px;
    height: 605px;
    background: var(--bordeaux);
  }
  .body-copy {
    position: absolute;
    left: 161px;
    top: 382px;
    width: 560px;
    font-size: 16.2px;
    line-height: 20.5px;
    letter-spacing: 0.55px;
    white-space: nowrap;
  }
  .body-copy p + p { margin-top: 20.5px; }
  .closing {
    position: absolute;
    left: 214px;
    top: 941px;
    font-size: 16.5px;
    letter-spacing: 0.8px;
  }
  .signature {
    position: absolute;
    left: 204px;
    top: 982px;
    width: 190px;
    height: 56px;
    background: var(--signature-tone);
    border-radius: 4px;
  }
  .sender {
    position: absolute;
    left: 213px;
    top: 1044px;
    font-size: 17px;
    font-weight: 700;
    letter-spacing: 0.4px;
    color: var(--bordeaux);
  }
</style>
</head>
<body>
<main class="letter">
  <div class="band band--top"></div>

  <p class="date">12.08.2016</p>

  <h1 class="subject" style="font-weight:300">Bewerbung um die Stelle als <span class="subject__role">Allroundtalent</span></h1>

  <p class="salutation">Sehr geehrte Damen und Herren,</p>

  <div class="accent-rule"></div>

  <div class="body-copy">
    <p>berum volorepel ipsume landa estem rehentis dolorero expe<br>
    seditionet faciis endebitae nates modi sintecatus natium ationse<br>
    quidusdam, od ut velignim audaepe rnatur? Quibuste consectiis<br>
    inimolo dolupienim as eiurectiam qui te nus magnit experesti-<br>
    bus aut earunt, versperore ra sitateniet exped qui verferis sunt,<br>
    quias unt quae con rernat dis sunt ut eatur apel maio tem aut.</p>
    <p>Restenim rerum il estiore, ommoluptio. Namus, officius volupta-<br>
    tus iust occatur. Ati officiae dusapid quae seniam rerit explabo<br>
    rrovit odignis trumqui od magnimporiam eat exceatisciae et<br>
    faccum quia nost, sitiatiatem hic to officii stionse quibusam eos-<br>
    simi, occulpa volorum neceaquiat.</p>
    <p>Minis et fugia desto dolupta tesersp eribusdae iurio. Fugit rehen-<br>
    da eperchil ea dolestio. Faceste cepremolo minulpa velit alia-<br>
    tur, accate cum, te eatinvel inveles a quias et eos eatecto eum<br>
    sitidolorende et facest everiamust rem alia perum doles sequiae<br>
    ctatatiis debis vel in estrupt aspercientum repe voluptam.</p>
    <p>Eaqui odit eum is voluptio. Cus restiur, con eum fugias quatur.<br>
    Tum aut ad ma non eiur, ommoluptae id modi tem none de res-<br>
    sitium antecaborem es nulparum que et et doluptati nimagnihici<br>
    optus aliqui odi id quatquias modi cum faci debitiore, ea aut<br>
    ipsumqui omnihitia dellor saperibus alit perrum fuga. Hentiat<br>
    autemporese cusam suntum accus doluptur, quo od qui tem ere</p>
  </div>

  <p class="closing">Mit freundlichen Grüßen</p>

  <div class="signature" role="img" aria-label="Handschriftliche Unterschrift"></div>

  <p class="sender">Heike Brandt</p>

  <div class="band band--bottom"></div>
</main>
</body>
</html>
```